The Velorind Project

All information regarding the design is located at Velorind.com. Any questions regarding the project, will be answered on the site.

```html
<!DOCTYPE html>
<html lang="en">
<head>
<meta charset="utf-8">
<title>Velorind</title>
<link rel="stylesheet" href="https://fonts.googleapis.com/css2?family=Ubuntu:wght@300;400;500&display=swap">
<style>
  :root {
    --bar-top: #5ccbf4;
    --bar-bottom: #3cb6ea;
    --tab-dark: #12729e;
    --tab-light: #f6f6f6;
    --page-bg: #f3f3f3;
    --brand-red: #d30f14;
    --mark-grey: #aca8a9;
    --field-border: #cfcfcf;
    --placeholder: #b4b4b4;
    --button-blue: #5aade4;
    --hint-grey: #9a9a9a;
    --footer-grey: #7a7a7a;
    --white: #ffffff;
  }
  * { box-sizing: border-box; margin: 0; padding: 0; }
  html, body {
    width: 1200px; height: 843px; overflow: hidden;
    background: var(--page-bg);
    font-family: "Ubuntu", sans-serif;
  }
  .page { position: relative; width: 1200px; height: 843px; }

  .top-bar {
    position: absolute; left: 0; top: 0; width: 1200px; height: 31px;
    background: linear-gradient(var(--bar-top), var(--bar-bottom));
  }
  .top-bar a { position: absolute; top: 8px; font-size: 13px; color: var(--white); text-decoration: none; line-height: 16px; }
  .tab { top: 3px !important; height: 28px; padding-top: 5px; text-align: center; border-radius: 3px 3px 0 0; }
  .tab-active { left: 112px; width: 83px; background: var(--tab-light); color: #333 !important; }
  .tab-community { left: 197px; width: 135px; background: var(--tab-dark); }
  .caret { display: inline-block; margin-left: 6px; vertical-align: 2px; border-left: 4px solid transparent; border-right: 4px solid transparent; border-top: 5px solid var(--white); }

  .brand {
    position: absolute; left: 0; top: 190px; width: 1200px;
    display: flex; justify-content: center; align-items: center; gap: 26px;
  }
  .brand-dot { width: 56px; height: 56px; border-radius: 50%; background: var(--mark-grey); }
  .brand-name { font-size: 96px; font-weight: 400; color: var(--brand-red); line-height: 110px; letter-spacing: -2px; }

  .ask-form {
    position: absolute; left: 273px; top: 306px; width: 654px; height: 42px;
    border: 1px solid var(--field-border); background: var(--white); display: flex;
  }
  .ask-icon { width: 56px; display: flex; align-items: center; justify-content: center; }
  .ask-input { flex: 1; font-size: 16px; font-weight: 300; color: var(--placeholder); line-height: 40px; }
  .ask-button {
    width: 122px; height: 40px; background: var(--button-blue); color: var(--white);
    font-family: inherit; font-size: 17px; border: none; letter-spacing: -0.3px;
  }
  .ask-hint {
    position: absolute; left: 0; top: 361px; width: 1106px; text-align: center;
    font-size: 12px; font-weight: 300; color: var(--hint-grey);
  }

  .footer { position: absolute; left: 0; top: 771px; width: 1200px; text-align: center; font-size: 12px; color: var(--footer-grey); font-weight: 300; }
  .footer-links a { color: var(--footer-grey); text-decoration: none; margin: 0 5px; }
  .copyright { margin-top: 5px; }
</style>
</head>
<body>
<div class="page">
  <nav class="top-bar">
    <a class="tab tab-active" href="#">Answers</a>
    <a class="tab tab-community" href="#">Q&amp;A Community</a>
    <a href="#" style="left:354px">Images</a>
    <a href="#" style="left:417px">News</a>
    <a href="#" style="left:471px">Video</a>
    <a href="#" style="left:526px">Local</a>
    <a href="#" style="left:578px">More<span class="caret"></span></a>
    <a href="#" style="left:879px">Login<span class="caret"></span></a>
    <a href="#" style="left:945px">Register</a>
    <a href="#" style="left:1027px">Contact Us</a>
  </nav>

  <div class="brand">
    <span class="brand-dot"></span>
    <span class="brand-name">Velorind</span>
  </div>

  <form class="ask-form">
    <span class="ask-icon">
      <svg width="22" height="22" viewBox="0 0 22 22" aria-hidden="true">
        <circle cx="9" cy="9" r="6.5" fill="none" stroke="#8f8f8f" stroke-width="2.5"/>
        <line x1="14" y1="14" x2="20" y2="20" stroke="#8f8f8f" stroke-width="3" stroke-linecap="round"/>
      </svg>
    </span>
    <span class="ask-input">Write your question here</span>
    <button class="ask-button" type="button">Ask question</button>
  </form>
  <p class="ask-hint">Example: Why is the sky blue?</p>

  <footer class="footer">
    <div class="footer-links">
      <a href="#">Home</a><a href="#">Question &amp; Answers</a><a href="#">Register</a><a href="#">Contact Us</a>
    </div>
    <div class="copyright">© Copyright Velorind. All Rights Reserved</div>
  </footer>
</div>
</body>
</html>
```